Business Card Re-design

We are looking for a fresh bold look for general office business cards. We are a staffing agency that staffs industrial, coal mining, and clerical jobs.
Tag Line: We match the BEST people with the BEST roles.
Harlow Office: 2473 W. Tallow Creek Rd, Harlow, IN - 47308
p. 555.203.6180 f. 555.203.6195
Westbrook Office: 264 S. Birch Ln, Westbrook, IN - 47152
p. 555.319.2047 f. 555.203.6195
Absentee/Emergency 24hr Hotline 555.203.6172 opt.1
www.bluelanternworkforce.example

```html
<!DOCTYPE html>
<html lang="en">
<head>
<meta charset="utf-8">
<title>Blue Lantern Workforce – Business Card</title>
<link href="https://fonts.googleapis.com/css2?family=Open+Sans:wght@400;600&display=swap" rel="stylesheet">
<style>
  :root {
    --page: #ffffff;
    --card: #1a1a1a;
    --brand-blue: #1d4f86;
    --brand-green: #3a9a44;
    --accent-green: #4cae4c;
    --band-navy: #1c2b4f;
    --text-light: #f2f2f2;
    --icon-green: #4cae4c;
  }
  * { margin: 0; padding: 0; box-sizing: border-box; }
  html, body {
    width: 1200px; height: 720px; overflow: hidden;
    background: var(--page);
    font-family: "Open Sans", Arial, sans-serif;
  }
  .card {
    position: absolute;
    width: 444px; height: 274px;
    background: var(--card);
    overflow: hidden;
  }
  .card--front { left: 106px; top: 208px; }
  .card--back  { left: 646px; top: 206px; }

  .wordmark {
    position: absolute;
    display: flex; align-items: center; gap: 14px;
  }
  .wordmark__square {
    width: 26px; height: 26px; background: var(--brand-green); flex: none;
  }
  .wordmark__name {
    color: var(--brand-blue);
    font-weight: 600;
    text-transform: uppercase;
    line-height: 1.02;
    letter-spacing: 0.5px;
  }
  .card--front .wordmark { left: 62px; top: 80px; }
  .card--front .wordmark__name { font-size: 40px; }
  .card--back .wordmark { left: 26px; top: 28px; gap: 9px; }
  .card--back .wordmark__square { width: 14px; height: 14px; }
  .card--back .wordmark__name { font-size: 19px; }

  .footer-band {
    position: absolute; left: 0; bottom: 0; width: 100%; height: 14px;
  }
  .footer-band svg { position: absolute; inset: 0; }
  .footer-band__text {
    position: absolute; right: 10px; bottom: 1px;
    font-size: 8.8px; color: var(--text-light); line-height: 12px;
    white-space: nowrap;
  }
  .footer-band__text--hotline { right: 44px; }

  .contact {
    position: absolute; left: 26px; top: 117px;
    color: var(--text-light); font-size: 8.6px; line-height: 11.5px;
  }
  .office + .office { margin-top: 14px; }
  .office__address { margin-bottom: 5px; }
  .contact-line {
    display: flex; align-items: center; gap: 5px;
    font-weight: 600; height: 12px;
  }
  .contact-line svg { width: 9px; height: 9px; flex: none; }
  .contact-line--web { font-weight: 400; margin-top: 13px; }
</style>
</head>
<body>

<section class="card card--front" aria-label="Card front">
  <div class="wordmark">
    <span class="wordmark__square"></span>
    <span class="wordmark__name">Blue<br>Lantern<br>Workforce</span>
  </div>
  <div class="footer-band">
    <svg width="444" height="14" viewBox="0 0 444 14">
      <rect x="0" y="11" width="216" height="3" fill="var(--accent-green)"/>
      <polygon points="218,0 444,0 444,14 210,14" fill="var(--band-navy)"/>
    </svg>
    <p class="footer-band__text">We match the BEST people with the BEST roles</p>
  </div>
</section>

<section class="card card--back" aria-label="Card back">
  <div class="wordmark">
    <span class="wordmark__square"></span>
    <span class="wordmark__name">Blue<br>Lantern<br>Workforce</span>
  </div>

  <div class="contact">
    <div class="office">
      <p class="office__address">Harlow Office: 2473 W. Tallow Creek Rd,<br>Harlow, IN - 47308</p>
      <p class="contact-line">
        <svg viewBox="0 0 10 10" aria-label="Phone"><path d="M2 0.5l1.8 2-1 1.2c.6 1.3 1.5 2.2 2.7 2.8l1.1-1 2 1.7-.9 1.8C4.5 9 .8 5.4.4 1.4z" fill="var(--icon-green)"/></svg>
        555.203.6180
      </p>
      <p class="contact-line">
        <svg viewBox="0 0 10 10" aria-label="Fax"><rect x="2.5" y="0.5" width="5" height="3" fill="none" stroke="var(--icon-green)"/><rect x="0.5" y="3.5" width="9" height="4" rx="1" fill="var(--icon-green)"/><rect x="2.5" y="6.5" width="5" height="3" fill="var(--card)" stroke="var(--icon-green)"/></svg>
        555.203.6195
      </p>
    </div>
    <div class="office">
      <p class="office__address">Westbrook Office: 264 S. Birch Ln,<br>Westbrook, IN - 47152</p>
      <p class="contact-line">
        <svg viewBox="0 0 10 10" aria-label="Phone"><path d="M2 0.5l1.8 2-1 1.2c.6 1.3 1.5 2.2 2.7 2.8l1.1-1 2 1.7-.9 1.8C4.5 9 .8 5.4.4 1.4z" fill="var(--icon-green)"/></svg>
        555.319.2047
      </p>
      <p class="contact-line">
        <svg viewBox="0 0 10 10" aria-label="Fax"><rect x="2.5" y="0.5" width="5" height="3" fill="none" stroke="var(--icon-green)"/><rect x="0.5" y="3.5" width="9" height="4" rx="1" fill="var(--icon-green)"/><rect x="2.5" y="6.5" width="5" height="3" fill="var(--card)" stroke="var(--icon-green)"/></svg>
        555.203.6195
      </p>
    </div>
    <p class="contact-line contact-line--web">
      <svg viewBox="0 0 10 10" aria-label="Website"><circle cx="5" cy="5" r="4.3" fill="none" stroke="var(--icon-green)"/><ellipse cx="5" cy="5" rx="1.8" ry="4.3" fill="none" stroke="var(--icon-green)" stroke-width="0.8"/><path d="M0.7 5h8.6M1.5 2.8h7M1.5 7.2h7" stroke="var(--icon-green)" stroke-width="0.8"/></svg>
      www.bluelanternworkforce.example
    </p>
  </div>

  <div class="footer-band">
    <svg width="444" height="14" viewBox="0 0 444 14">
      <rect x="0" y="11" width="212" height="3" fill="var(--accent-green)"/>
      <polygon points="220,0 444,0 444,14 210,14" fill="var(--band-navy)"/>
    </svg>
    <p class="footer-band__text footer-band__text--hotline">24hr Hotline 555.203.6172 opt.1</p>
  </div>
</section>

</body>
</html>
```